Stylish Business Cards Wanted

- DOUBLE SIDED Design Required -

High end, edgy cards for a corporate and personal stylist. Must include logo,
Name: Belinda Forsey
Title: Director and Stylist
telephone : +61 8 8217 4592
email: belinda@thegarbledger.example
website: thegarbledger.example
Tag: Corporate Workwear & Uniform Specialist | Personal Stylist
Would like nice icons for telephone, email, website

Target Market(s)

Businesses wanting stylish uniforms, people wanting stylish wardrobes

Industry/Entity Type

Corporate Workwear Stylist

Contact Information for Business Card

I would like black, white and gold foiling incorporated in the design - possibly a touch of the other colours on my branding guide attached Name: Belinda Forsey Title: Director and Stylist telephone : +61 8 8217 4592 email: belinda@thegarbledger.example website: thegarbledger.example Tag: Corporate Workwear & Uniform Specialist | Personal Stylist Would like nice icons for telephone, email, website

Font styles to use
Other font styles liked:
• Raleway

Colors

Designer to choose colors to be used in the design.

Requirements
Must have
• Gold foil accents

```html
<!DOCTYPE html>
<html lang="en">
<head>
<meta charset="utf-8">
<title>The Garb Ledger – Business Cards</title>
<link href="https://fonts.googleapis.com/css2?family=Open+Sans:wght@400;600&display=swap" rel="stylesheet">
<style>
  :root {
    --backdrop: #262626;
    --card: #151515;
    --gold: #d9cb8c;
    --gold-light: #f3ecc0;
    --gold-deep: #9e8a4a;
    --font: "Open Sans", sans-serif;
  }
  * { box-sizing: border-box; margin: 0; padding: 0; }
  html, body {
    width: 1200px; height: 900px; overflow: hidden;
    background: var(--backdrop);
    font-family: var(--font);
  }
  .sheet {
    width: 1200px; height: 900px;
    display: flex; flex-direction: column;
    align-items: center; justify-content: center; gap: 56px;
  }
  .card {
    position: relative;
    width: 620px; height: 370px;
    background: var(--card);
    box-shadow: 0 12px 30px rgba(0,0,0,.5);
    overflow: hidden;
  }
  .card::after {
    content: "";
    position: absolute; left: 0; right: 0; bottom: 0; height: 6px;
    background: linear-gradient(90deg, var(--gold-deep), var(--gold-light) 45%, var(--gold) 70%, var(--gold-deep));
  }
  .brand-name {
    color: var(--gold);
    font-weight: 600;
    line-height: 1.05;
    letter-spacing: .02em;
  }
  .brand-mark {
    display: inline-block;
    width: 14px; height: 14px;
    border-radius: 50%;
    background: var(--gold);
    vertical-align: middle;
    margin-right: 12px;
  }

  /* Front face */
  .card-front .brand-name {
    position: absolute; left: 250px; top: 96px;
    font-size: 46px; text-align: left;
  }
  .tagline {
    position: absolute; left: 40px; right: 40px; bottom: 34px;
    color: var(--gold); font-size: 17px; text-align: center;
    letter-spacing: .01em;
  }
  .tagline .dot { margin: 0 12px; }

  /* Back face */
  .card-back .brand-name {
    position: absolute; left: 150px; top: 44px;
    font-size: 30px;
  }
  .rule {
    position: absolute; left: 60px; right: 40px; height: 1px;
    background: var(--gold);
  }
  .rule-top { top: 150px; }
  .rule-bottom { bottom: 48px; left: 60px; }
  .contact-list {
    position: absolute; left: 60px; top: 176px;
    list-style: none; color: var(--gold); font-size: 17px;
  }
  .contact-list li { display: flex; align-items: center; gap: 10px; margin-bottom: 6px; }
  .contact-list svg { width: 14px; height: 14px; flex: none; }
  .person {
    position: absolute; right: 50px; bottom: 72px; text-align: left;
    color: var(--gold);
  }
  .person-name { font-weight: 600; font-size: 24px; letter-spacing: .02em; text-transform: uppercase; }
  .person-title { font-size: 17px; margin-left: 36px; }
</style>
</head>
<body>
<main class="sheet">
  <section class="card card-front" aria-label="Card front">
    <p class="brand-name"><span class="brand-mark"></span>The Garb<br>Ledger</p>
    <p class="tagline">Corporate Workwear &amp; Uniform Specialist<span class="dot">•</span>Personal Stylist</p>
  </section>

  <section class="card card-back" aria-label="Card back">
    <p class="brand-name"><span class="brand-mark"></span>The Garb Ledger</p>
    <div class="rule rule-top"></div>
    <ul class="contact-list">
      <li>
        <svg viewBox="0 0 16 16" aria-hidden="true"><path fill="var(--gold)" d="M3.5 1.5l2.5 0 1.2 3-1.6 1.2c.8 1.8 2.4 3.4 4.2 4.2l1.2-1.6 3 1.2v2.5c0 .8-.7 1.5-1.5 1.5C6.7 13.5 2.5 9.3 2 3c0-.8.7-1.5 1.5-1.5z"/></svg>
        +61 8 8217 4592
      </li>
      <li>
        <svg viewBox="0 0 16 16" aria-hidden="true"><rect x="1.5" y="3.5" width="13" height="9" fill="none" stroke="var(--gold)" stroke-width="1.4"/><path d="M1.5 3.5l6.5 5 6.5-5" fill="none" stroke="var(--gold)" stroke-width="1.4"/></svg>
        belinda@thegarbledger.example
      </li>
      <li>
        <svg viewBox="0 0 16 16" aria-hidden="true"><g fill="none" stroke="var(--gold)" stroke-width="1.3"><circle cx="8" cy="8" r="6.3"/><ellipse cx="8" cy="8" rx="2.8" ry="6.3"/><path d="M1.7 8h12.6"/></g></svg>
        thegarbledger.example
      </li>
    </ul>
    <div class="person">
      <p class="person-name">Belinda Forsey</p>
      <p class="person-title">Director and Stylist</p>
    </div>
    <div class="rule rule-bottom"></div>
  </section>
</main>
</body>
</html>
```